We have developed a fully functional App called Corvalink. However, it requires a nicer GUI. You can see screenshots of our App on www.corvalink-example.com under "Tutorial". For those of you with Android, you can also install it. When you go to Corvalink-example.com, your phone will automatically redirect you to download. From there, you'll get a better idea of what our App looks like and how your design can make it way better. Please note we expect a design idea for most screens (there's about 8 screens) but do just one screen first and if you win, you can do the other 8 after.

Target Market(s)

People looking for dating / flirting

Industry/Entity Type

Android

Requirements
Must have
• sleek looking

```html
<!DOCTYPE html>
<html lang="en">
<head>
<meta charset="utf-8">
<title>Corvalink – Profile</title>
<link rel="stylesheet" href="https://fonts.googleapis.com/css2?family=Antonio:wght@100;200&family=Roboto:wght@300;400&display=swap">
<style>
:root{
  --magenta:#960064;
  --magenta-dark:#7e0054;
  --magenta-bright:#d1109a;
  --page:#f3f0ed;
  --card:#ffffff;
  --text-grey:#8a8680;
  --line:#e2d3dc;
  --white:#ffffff;
}
*{box-sizing:border-box;margin:0;padding:0}
html,body{width:778px;height:1200px;overflow:hidden}
body{background:var(--page);font-family:'Roboto',sans-serif;position:relative;color:var(--text-grey)}
.app-bar{position:absolute;left:0;top:0;width:778px;height:99px;background:var(--magenta);box-shadow:0 2px 4px rgba(0,0,0,.3);z-index:2}
.app-bar .action{position:absolute;top:0;height:99px;display:flex;align-items:center;justify-content:center}
.app-bar .back{left:0;width:70px}
.app-bar .search{left:556px;width:108px;border-left:1px solid var(--magenta-dark)}
.app-bar .menu{left:664px;width:114px;border-left:1px solid var(--magenta-dark)}
.cover{position:absolute;left:0;top:99px;width:778px;height:430px;background:radial-gradient(ellipse at 70% 40%,#b49a86 0%,#6e5548 40%,#2f2226 80%,#1e161a 100%)}
.avatar{position:absolute;left:108px;top:359px;width:132px;height:132px;border-radius:50%;background:radial-gradient(circle at 45% 40%,#cdb497,#6d5444 70%,#2b2022);border:2px solid rgba(255,255,255,.2)}
.avatar-stem{position:absolute;left:172px;top:491px;width:6px;height:38px;background:rgba(255,255,255,.35)}
.profile-name{position:absolute;left:259px;top:406px;color:var(--white);font-size:26px;font-weight:400;letter-spacing:.3px}
.profile-meta{position:absolute;left:260px;top:440px;color:#e8e0e6;font-size:16px;font-weight:300}
.profile-meta b{font-weight:400;color:var(--white)}
.tagline{position:absolute;left:0;top:529px;width:778px;height:132px;background:var(--card);box-shadow:0 1px 2px rgba(0,0,0,.15);text-align:center}
.tagline p{position:absolute;left:0;width:778px;top:52px;font-size:27px;font-weight:300;letter-spacing:1px;color:#8f8b86}
.tagline .q{position:absolute;top:40px;font-family:'Antonio',sans-serif;font-size:34px;color:#b8b3ad}
.details{position:absolute;left:23px;top:693px;width:734px;height:327px;background:var(--card);border-radius:4px;box-shadow:0 1px 3px rgba(0,0,0,.15)}
.stat{position:absolute;text-align:center;font-family:'Antonio',sans-serif;color:#8f8b86}
.stat .big{font-weight:100;font-size:66px;line-height:1;display:block}
.stat .label{font-weight:200;font-size:20px;display:block;letter-spacing:.3px;margin-top:2px}
.stat.status{left:20px;top:26px;width:112px}
.stat.open-to{left:156px;top:26px;width:452px}
.stat.age{left:616px;top:26px;width:104px}
.stat.height{left:616px;top:140px;width:104px}
.divider{position:absolute;background:var(--line)}
.bio{position:absolute;left:29px;top:150px;width:570px;font-size:26px;font-weight:300;line-height:34px;color:#8f8b86;letter-spacing:.3px}
.more{position:absolute;left:0;top:254px;width:734px;text-align:center;font-size:20px;letter-spacing:1.5px;color:#6f6b67}
.fab{position:absolute;border-radius:50%;background:radial-gradient(circle at 50% 30%,var(--magenta-bright),var(--magenta) 75%);box-shadow:0 3px 6px rgba(0,0,0,.3);display:flex;align-items:center;justify-content:center;border:2px solid rgba(255,255,255,.4)}
.fab.small{width:66px;height:66px}
.fab.close{width:122px;height:122px;left:327px;top:1051px;box-shadow:0 6px 16px rgba(0,0,0,.3)}
</style>
</head>
<body>
<header class="app-bar">
  <div class="action back"><svg width="34" height="46" viewBox="0 0 34 46"><path d="M28 4 8 23l20 19" fill="none" stroke="#fff" stroke-width="7" stroke-linecap="round" stroke-linejoin="round"/></svg></div>
  <div class="action search"><svg width="42" height="42" viewBox="0 0 42 42"><circle cx="18" cy="18" r="13" fill="none" stroke="#fff" stroke-width="5"/><path d="M28 28l10 10" stroke="#fff" stroke-width="6" stroke-linecap="round"/></svg></div>
  <div class="action menu"><svg width="12" height="42" viewBox="0 0 12 42"><rect x="1" y="1" width="10" height="9" fill="#fff"/><rect x="1" y="16" width="10" height="9" fill="#fff"/><rect x="1" y="31" width="10" height="9" fill="#fff"/></svg></div>
</header>

<section class="cover" role="img" aria-label="Cover photo of the profile member"></section>
<div class="avatar-stem"></div>
<div class="avatar" role="img" aria-label="Profile photo of the member"></div>
<h1 class="profile-name">SENSUAL LARISSA</h1>
<p class="profile-meta"><b>F</b> / BI-CURIOUS / 25</p>

<section class="tagline">
  <span class="q" style="left:78px">“</span>
  <p>GODDESS AND TEMTRESS LIVES HERE</p>
  <span class="q" style="left:680px">”</span>
</section>

<section class="details">
  <div class="stat status"><span class="big">OPEN</span><span class="label">RELATIONSHIP</span></div>
  <div class="divider" style="left:153px;top:14px;width:1px;height:110px"></div>
  <div class="stat open-to"><span class="big">FWB, MAYBE MORE</span><span class="label">OPEN TO</span></div>
  <div class="divider" style="left:613px;top:14px;width:1px;height:210px"></div>
  <div class="stat age"><span class="big">25</span><span class="label">FEMALE</span></div>
  <div class="divider" style="left:20px;top:124px;width:584px;height:1px"></div>
  <div class="divider" style="left:613px;top:124px;width:100px;height:1px"></div>
  <p class="bio">I love volley ball. I love animals and I am a vegetarian</p>
  <div class="stat height"><span class="big">5.4</span><span class="label">INCHES</span></div>
  <div class="divider" style="left:0;top:254px;width:734px;height:1px"></div>
  <p class="more" style="top:268px">VIEW MORE ABOUT ME</p>
</section>

<div class="fab small" style="left:237px;top:955px" aria-label="Send gift"><svg width="32" height="32" viewBox="0 0 32 32" fill="none" stroke="#fff" stroke-width="2"><rect x="4" y="11" width="24" height="6"/><rect x="6" y="17" width="20" height="12"/><path d="M16 11v18M16 11c-3-6-9-6-7-1M16 11c3-6 9-6 7-1"/></svg></div>
<div class="fab small" style="left:355px;top:924px" aria-label="Add friend"><svg width="34" height="34" viewBox="0 0 34 34" fill="none" stroke="#fff" stroke-width="2.2"><circle cx="14" cy="11" r="6"/><path d="M3 29c0-7 5-11 11-11s8 3 9 5"/><path d="M26 20v10M21 25h10"/></svg></div>
<div class="fab small" style="left:462px;top:955px" aria-label="Call"><svg width="32" height="32" viewBox="0 0 32 32" fill="none" stroke="#fff" stroke-width="2.2" stroke-linejoin="round"><path d="M8 4l5 6-3 3c2 4 5 7 9 9l3-3 6 5-3 4C15 28 4 17 4 7z"/></svg></div>
<div class="fab small" style="left:193px;top:1048px" aria-label="More options"><svg width="36" height="10" viewBox="0 0 36 10" fill="none" stroke="#fff" stroke-width="2"><circle cx="6" cy="5" r="3.5"/><circle cx="18" cy="5" r="3.5"/><circle cx="30" cy="5" r="3.5"/></svg></div>
<div class="fab small" style="left:511px;top:1048px" aria-label="Message"><svg width="34" height="32" viewBox="0 0 34 32" fill="none" stroke="#fff" stroke-width="2.2" stroke-linejoin="round"><path d="M17 4C9 4 3 9 3 15c0 4 3 7 6 8l-1 6 7-5h2c8 0 14-4 14-9S25 4 17 4z"/></svg></div>
<div class="fab close" aria-label="Close"><svg width="32" height="32" viewBox="0 0 32 32"><path d="M6 6l20 20M26 6 6 26" stroke="#5a0b3e" stroke-width="7" stroke-linecap="round"/></svg></div>
</body>
</html>
```